Flyer-Design für Lindenblüten Abend Kurs Vol. 2
Zielgruppe
Seminare, Vorträge , Therapien, Beratung, Coaching
WEchseljahre Beratung
Sexualtherapie, Sexualberatung
Mentaltraining
Es soll Frauen gefallen und ermuntern zum Seminar zu kommen, frü Thema Wechseljahre interessieren
Aufgabenstellung
Grösse A5 Hochkant

```html
<!DOCTYPE html>
<html lang="de">
<head>
<meta charset="utf-8">
<title>Lindenblüten Abend Kurs Vol. 2</title>
<link rel="stylesheet" href="https://fonts.googleapis.com/css2?family=Open+Sans:wght@400;600&family=Bellefair&family=Parisienne&display=swap">
<style>
  :root {
    --ink: #464646;
    --body-ink: #555555;
    --sky: #4fc6e3;
    --sky-deep: #36b3d4;
    --rose: #d98bb6;
    --rose-ring: #d67fb0;
    --slate: #8ea6ae;
    --paper: #fbfbfc;
    --white: #ffffff;
  }
  * { box-sizing: border-box; margin: 0; padding: 0; }
  html, body { width: 872px; height: 1200px; overflow: hidden; background: var(--paper); }
  body { font-family: "Open Sans", Arial, sans-serif; color: var(--ink); }
  .flyer { position: relative; width: 872px; height: 1200px; overflow: hidden; background: var(--paper); }

  .photo-portrait-top {
    position: absolute; left: 520px; top: 0; width: 352px; height: 400px;
    background:
      linear-gradient(90deg, var(--paper) 0%, rgba(251,251,252,0) 22%),
      radial-gradient(ellipse at 55% 45%, #d7c9bf 0%, #b9b2aa 40%, #9fb9c9 75%, #c9dfe9 100%);
  }
  .wave { position: absolute; left: 0; top: 300px; width: 872px; height: 280px; }

  .headline { position: absolute; left: 50px; top: 46px; white-space: nowrap; }
  .headline .invite { font-size: 33px; line-height: 44px; }
  .headline .date { font-size: 33px; line-height: 50px; }
  .headline .title { font-size: 45px; font-weight: 600; line-height: 68px; }
  .headline .series { font-size: 33px; line-height: 48px; }

  .slogan {
    position: absolute; left: 205px; top: 278px;
    font-family: "Parisienne", cursive; color: var(--sky-deep);
    font-size: 31px; line-height: 38px;
  }
  .slogan span { display: block; }
  .slogan span + span { padding-left: 10px; }

  .photo-circle-left {
    position: absolute; left: -119px; top: 291px; width: 360px; height: 360px;
    border-radius: 50%; border: 5px solid var(--rose-ring);
    background: radial-gradient(circle at 60% 40%, #e8cdb8 0%, #a9b3d6 45%, #7f8fc0 70%, #b9c7a4 100%);
  }

  .trainer {
    position: absolute; left: 300px; top: 373px; width: 198px; height: 198px;
    border-radius: 50%; background: var(--rose); border: 7px solid var(--white);
    color: var(--white); text-align: center; padding-top: 40px;
  }
  .trainer .name { font-size: 21px; line-height: 30px; white-space: nowrap; }
  .trainer .roles { font-size: 12.5px; line-height: 18px; margin-top: 10px; }

  .org-badge {
    position: absolute; left: 656px; top: 278px; width: 150px; height: 150px;
    border-radius: 50%; background: var(--sky); border: 3px solid var(--white);
    display: flex; align-items: center; justify-content: center; text-align: center;
    color: var(--white); font-size: 15px; font-weight: 600; line-height: 20px;
  }

  .band-note {
    position: absolute; left: 560px; top: 446px; width: 240px; text-align: center;
    color: var(--white); font-size: 16.5px; line-height: 22px;
  }

  .photo-portrait-bottom {
    position: absolute; left: 0; top: 600px; width: 436px; height: 600px;
    border-radius: 0 190px 0 0;
    background: radial-gradient(ellipse at 50% 30%, #e6c2a8 0%, #c99b85 25%, #5aa9c4 55%, #2c2f3a 85%);
  }

  .content { position: absolute; left: 451px; top: 568px; width: 375px; }
  .content h2 {
    font-family: "Bellefair", Georgia, serif; font-weight: 400;
    font-size: 28px; line-height: 31px; color: #2f2f2f; white-space: nowrap;
  }
  .content p { margin-top: 28px; width: 365px; font-size: 16px; line-height: 24px; color: var(--body-ink); }

  .info-box {
    position: absolute; left: 444px; top: 973px; width: 428px; height: 158px;
    background: var(--sky); color: var(--white);
    padding: 25px 48px 0 52px; font-size: 16px; line-height: 22px;
  }
  .footer-band {
    position: absolute; left: 471px; top: 1152px; width: 401px; height: 48px;
    background: var(--slate);
  }
  .footer-band .web {
    position: absolute; right: 34px; top: 0; color: var(--white); font-size: 16px; line-height: 26px;
  }
</style>
</head>
<body>
<main class="flyer">
  <div class="photo-portrait-top" role="img" aria-label="Portrait einer älteren Frau mit grauem Haar, lächelnd nach oben blickend"></div>

  <svg class="wave" viewBox="0 0 872 280" aria-hidden="true">
    <defs>
      <linearGradient id="bandFill" x1="0" y1="0" x2="1" y2="1">
        <stop offset="0" stop-color="#6fd0ea"/>
        <stop offset="0.5" stop-color="#a3b7df"/>
        <stop offset="1" stop-color="#b79bd0"/>
      </linearGradient>
    </defs>
    <path d="M200 140 C320 130 420 110 520 80 C640 40 760 10 872 25 L872 240 C760 218 650 205 520 215 C400 225 300 240 200 245 Z" fill="url(#bandFill)"/>
    <path d="M200 245 C300 240 400 225 520 215 C650 205 760 218 872 240 L872 252 C760 226 650 214 520 222 C400 232 300 248 200 254 Z" fill="#36b3d4"/>
  </svg>

  <header class="headline">
    <div class="invite">Seien auch Sie mit dabei am</div>
    <div class="date">23.04.2017</div>
    <h1 class="title">Lindenblüten Abend</h1>
    <div class="series">Kurs - Vol. 2</div>
  </header>

  <div class="slogan"><span>Heiss Geschüttelt,</span><span>nicht kalt gerührt</span></div>

  <div class="photo-circle-left" role="img" aria-label="Foto einer blonden Frau in blauer Strickjacke, im Freien sitzend"></div>

  <div class="trainer">
    <div class="name">Mira Holdegger</div>
    <div class="roles">Sexualtherapeutin<br>Dipl. Wechseljahrberaterin<br>Mentaltrainerin</div>
  </div>

  <div class="org-badge">Fachstelle<br>Lindenweg</div>

  <div class="band-note">Mit noch mehr Antworten und Tipps für diese spannende Zeit</div>

  <div class="photo-portrait-bottom" role="img" aria-label="Foto einer fröhlichen älteren Frau mit türkisfarbenem Schal, Daumen hoch"></div>

  <section class="content">
    <h2>Über Abschied, Umbruch,<br>Sinnorientierung und Neuanfang.</h2>
    <p>Die Wechseljahre sind keine Krankheit und sie kommen nicht über Nacht. Sie sind eine Einladung an uns Frauen, uns in den vielfältigen Veränderungen, die sich in Körper, Geist und Seele vollziehen, neu zu erfahren. Unsere wahre Schönheit und unser sinnliches Erleben sind von äußeren Dingen unabhängig und blühen gerade im Älterwerden auf eine neue und besondere Weise auf! Das Seminar zeigt auf, in welcher Form uns dabei die Hormone sogar unterstützen.</p>
  </section>

  <div class="info-box">Ein spannendes Tagesseminar über die Wechselbäder der Gefühle, über Hormone, Orientierung, Hilfen und Möglichkeiten. Über die Zeit davor, mittendrin und danach.</div>

  <footer class="footer-band"><span class="web">www.herzwege-kurs.ch</span></footer>
</main>
</body>
</html>
```